We need business cards for Tarnwick Consulting. We have a logo that was recently designed. I would obviously like the logo on the card and to stay with similar fonts and colors.

I think the font is Trebuchet MS or something very close to it.
CMYK for the blue is C:100 M:100 Y:0 K:0
And for the green C:40 M:0 Y:40 K:0

Tarnwick Consulting is based in Wellington, New Zealand. Doing consulting and advisory work in Australia, PNG and NZ to government and private organisations.
We provide management guidance and consultancy on petroleum, gas and mineral (predominantly gold) projects. (Geophysical consulting).
We advise on design, contractor selection, tendering, risk assessment through to full project delivery and operational management

We are looking for a professional, corporate looking cards.

Industry/Entity Type

Business

```html
<!DOCTYPE html>
<html lang="en">
<head>
<meta charset="utf-8">
<title>Tarnwick Consulting – Double-sided Business Card</title>
<link rel="stylesheet" href="https://fonts.googleapis.com/css2?family=PT+Sans:wght@400;700&display=swap">
<style>
  :root {
    --navy: #1b1464;
    --blue: #2e3192;
    --blue-light: #4a5bb0;
    --blue-deep: #232a7e;
    --green: #8dc63f;
    --green-soft: #a6d76e;
    --brand-text: #3b3c97;
    --white: #ffffff;
    --page: #ffffff;
    --caption: #333333;
  }
  * { box-sizing: border-box; margin: 0; padding: 0; }
  html, body { width: 964px; height: 1200px; overflow: hidden; background: var(--page); }
  body { position: relative; font-family: "PT Sans", "Trebuchet MS", sans-serif; }

  .card {
    position: absolute;
    left: 128px;
    width: 706px;
    height: 384px;
    overflow: hidden;
    box-shadow: 4px 6px 12px rgba(0,0,0,0.35);
  }

  /* Front */
  .card--front { top: 181px; background: linear-gradient(180deg, var(--blue-light) 40%, var(--blue) 70%, var(--blue-deep) 100%); }
  .card--front .top-band {
    position: absolute; left: 0; top: 0; width: 100%; height: 72px;
    background: linear-gradient(180deg, var(--navy) 0%, #262a86 100%);
  }
  .card--front .brand-band {
    position: absolute; left: 0; top: 72px; width: 100%; height: 140px;
    background: var(--white);
    box-shadow: 0 14px 20px rgba(20,20,80,0.35);
  }
  .card--front .brand {
    position: absolute; left: 70px; top: 116px;
  }
  .card--front .website {
    position: absolute; left: 0; right: 0; top: 308px;
    text-align: center; color: var(--white);
    font-size: 30px; letter-spacing: 0.2px;
  }

  .brand { display: flex; align-items: center; gap: 22px; }
  .brand__dot { width: 50px; height: 50px; border-radius: 50%; background: var(--green); }
  .brand__name { color: var(--brand-text); font-size: 46px; font-weight: 400; line-height: 1; }

  /* Back */
  .card--back { top: 634px; background: linear-gradient(180deg, #5a73c2 0%, var(--blue) 45%, var(--blue-deep) 100%); }
  .card--back .info-band {
    position: absolute; left: 0; top: 0; width: 100%; height: 122px;
    background: var(--white);
    border-bottom: 6px solid var(--green-soft);
  }
  .card--back .footer-band {
    position: absolute; left: 0; bottom: 0; width: 100%; height: 28px;
    background: var(--green);
  }
  .person { position: absolute; left: 46px; top: 44px; color: var(--navy); }
  .person__name { font-size: 24px; font-weight: 700; line-height: 1.1; }
  .person__role { font-size: 22px; color: var(--blue); line-height: 1.2; }
  .card--back .brand { position: absolute; left: 338px; top: 46px; gap: 14px; }
  .card--back .brand__dot { width: 30px; height: 30px; }
  .card--back .brand__name { font-size: 28px; }

  .contact {
    position: absolute; left: 46px; top: 156px;
    list-style: none; color: var(--white);
    font-size: 20px; line-height: 24.5px;
  }

  .caption {
    position: absolute; left: 0; right: 0; top: 1160px;
    text-align: center; color: var(--caption);
    font-size: 13px; line-height: 16px;
  }
</style>
</head>
<body>

<section class="card card--front" aria-label="Business card front">
  <div class="top-band"></div>
  <div class="brand-band"></div>
  <div class="brand">
    <span class="brand__dot"></span>
    <span class="brand__name">Tarnwick Consulting</span>
  </div>
  <p class="website">www.tarnwickconsulting.co.nz</p>
</section>

<section class="card card--back" aria-label="Business card back">
  <div class="info-band"></div>
  <div class="person">
    <p class="person__name">Maren Ashby</p>
    <p class="person__role">Director</p>
  </div>
  <div class="brand">
    <span class="brand__dot"></span>
    <span class="brand__name">Tarnwick Consulting</span>
  </div>
  <ul class="contact">
    <li>+64 4 5550142</li>
    <li>+64 21 555013</li>
    <li>14 Kowhai Rise</li>
    <li>Harbourview 6035</li>
    <li>Wellington</li>
    <li>New Zealand</li>
    <li>Maren@tarnwickconsulting.co.nz</li>
  </ul>
  <div class="footer-band"></div>
</section>

<p class="caption">tarnwick consulting<br>Double-sided Business Card Design</p>

</body>
</html>
```